Bright-loop stitchworks Business Card

embroidery printing

Target Market(s)

Businesses and public

Industry/Entity Type

Business

Contact Information for Business Card

Front of card..... Bright-loop stitchworks .... Dorian Felkway..... 868 512-7743.... Email... bright_loopstitchworks@mailvane.net

Back of card..... Bright-loop stitchworks embroidery & artwork

Colors
000000

```html
<!DOCTYPE html>
<html lang="en">
<head>
<meta charset="utf-8">
<title>Bright-loop stitchworks — Business Card</title>
<link rel="stylesheet" href="https://fonts.googleapis.com/css2?family=PT+Sans:wght@400;700&display=swap">
<style>
  :root {
    --backdrop: #a4a4a4;
    --paper: #f4f4f6;
    --ink: #000000;
    --ink-soft: #222222;
    --text-grey: #555555;
    --accent-red: #7a1209;
    --reverse-white: #f2f2f2;
    --rule-grey: #555555;
    --dot-1: #c8463a;
    --dot-2: #3b5693;
    --dot-3: #2a9fd6;
    --dot-4: #1d6f9f;
  }
  * { margin: 0; padding: 0; box-sizing: border-box; }
  html, body {
    width: 1105px; height: 1200px; overflow: hidden;
    background: var(--backdrop);
    font-family: "PT Sans", Arial, sans-serif;
  }
  .canvas { position: relative; width: 1105px; height: 1200px; }
  .card {
    position: absolute; left: 179px; width: 747px; height: 425px; overflow: hidden;
  }
  .card--front { top: 119px; background: var(--paper); }
  .card--back { top: 636px; background: var(--ink); }

  .brand-name {
    position: absolute; font-weight: 700; line-height: 1;
    letter-spacing: 0.5px; white-space: nowrap;
  }
  .card--front .brand-name { left: 46px; top: 62px; font-size: 46px; color: var(--ink); }
  .card--back .brand-name {
    left: 0; right: 0; top: 168px; text-align: center;
    font-size: 46px; color: var(--reverse-white);
  }

  .holder { position: absolute; left: 47px; top: 250px; }
  .holder__name { font-size: 26px; font-weight: 700; color: var(--accent-red); line-height: 1.15; }
  .holder__role { font-size: 21px; color: var(--ink-soft); line-height: 1.2; }

  .contact { position: absolute; left: 377px; top: 251px; list-style: none; }
  .contact__row {
    display: flex; align-items: center; gap: 10px;
    height: 29px; font-size: 19px; color: var(--text-grey);
  }
  .contact__icon { width: 17px; height: 17px; flex: none; }

  .footer-band { position: absolute; left: 0; bottom: 0; width: 747px; height: 28px; }

  .social {
    position: absolute; left: 0; right: 0; top: 325px;
    display: flex; justify-content: center; align-items: center; gap: 6px;
  }
  .social__rule { width: 70px; height: 1px; background: var(--rule-grey); }
  .social__dot { width: 32px; height: 32px; border-radius: 50%; }
  .social__dot--1 { background: var(--dot-1); }
  .social__dot--2 { background: var(--dot-2); }
  .social__dot--3 { background: var(--dot-3); }
  .social__dot--4 { background: var(--dot-4); }
  .tagline {
    position: absolute; left: 0; right: 0; top: 368px; text-align: center;
    font-size: 13px; color: var(--ink-soft); letter-spacing: 1px;
  }
</style>
</head>
<body>
<main class="canvas">
  <section class="card card--front" aria-label="Business card front">
    <div class="brand-name">Bright-loop stitchworks</div>

    <div class="holder">
      <p class="holder__name">Dorian Felkway</p>
      <p class="holder__role">CEO/Founder</p>
    </div>

    <ul class="contact">
      <li class="contact__row">
        <svg class="contact__icon" viewBox="0 0 24 24"><path fill="var(--accent-red)" d="M6.6 10.8a15 15 0 0 0 6.6 6.6l2.2-2.2c.3-.3.7-.4 1-.2 1.1.4 2.3.6 3.6.6.6 0 1 .4 1 1V20c0 .6-.4 1-1 1C10.6 21 3 13.4 3 4c0-.6.4-1 1-1h3.5c.6 0 1 .4 1 1 0 1.3.2 2.5.6 3.6.1.3 0 .7-.2 1z"/></svg>
        <span>868 512-7743</span>
      </li>
      <li class="contact__row">
        <svg class="contact__icon" viewBox="0 0 24 24"><rect x="2" y="5" width="20" height="14" fill="var(--accent-red)"/><path d="M2 5l10 8 10-8" fill="none" stroke="var(--paper)" stroke-width="1.8"/></svg>
        <span>bright_loopstitchworks@mailvane.net</span>
      </li>
      <li class="contact__row">
        <svg class="contact__icon" viewBox="0 0 24 24"><circle cx="12" cy="12" r="10" fill="var(--accent-red)"/><path d="M2 12h20M12 2c3 3 3 17 0 20M12 2c-3 3-3 17 0 20" fill="none" stroke="var(--paper)" stroke-width="1.3"/></svg>
        <span>www.brightloopstitch.net</span>
      </li>
    </ul>

    <svg class="footer-band" viewBox="0 0 747 28" preserveAspectRatio="none">
      <polygon points="0,0 486,0 478,28 0,28" fill="var(--ink)"/>
      <polygon points="494,0 747,0 747,28 486,28" fill="var(--accent-red)"/>
    </svg>
  </section>

  <section class="card card--back" aria-label="Business card back">
    <div class="brand-name">Bright-loop stitchworks</div>

    <div class="social">
      <span class="social__rule"></span>
      <span class="social__dot social__dot--1"></span>
      <span class="social__dot social__dot--2"></span>
      <span class="social__dot social__dot--3"></span>
      <span class="social__dot social__dot--4"></span>
      <span class="social__rule"></span>
    </div>
    <p class="tagline">Bright-loop stitchworks embroidery &amp; artwork</p>
  </section>
</main>
</body>
</html>
```